Kestrel Summit 2019 Enemies of the End-Times Church Flyer

We want a church conference flyer designed. We are looking for a professional, yet catchy design that uses our brand colors and logo creatively while communicating key information of the event effectively. <br/>The flyer must include all of the following:<br/>Title: Kestrel Summit 2019<br/>Topic: The Enemies of The End-Times Church <br/>Subtitles: <br/> -How the antichrist raises an army by social behavior engineering. <br/>-How the architects of modern social constructs escaped the church's radar. <br/>-The Holy Spirit's end-times agenda:<br/> The Knock-Out Punch!<br/>Speaker: Prophet Marcus Toliver <br/>Dates/time: December 27, 28 & 29 at 6pm<br/>Location: Halvorn Community Center <br/> 241 Pellham Street <br/> Portland, ME 04102<br/>Contact info: phone: 207-555-0148 <br/>email: contact@brookmeadow.example <br/> www.vutel.example<br/>*The flyer must also include a picture of the speaker and our Vutel logo <br/>Thanks, we look forward to seeing what you come up with!

Colors

Designer to choose colors to be used in the design.

Requirements
Must have
• The flyer must include all of the following:
• Title: Kestrel Summit 2019
• Topic: The Enemies of The End-Times Church
• Subtitles:
• -How the antichrist raises an army by social behavior engineering.
• -How the architects of modern social constructs escaped the church's radar.
• -The Holy Spirit's end-times agenda:
• The Knock-Out Punch!
• Speaker: Prophet Marcus Toliver
• Dates/time: December 27, 28 & 29 at 6pm
• Location: Halvorn Community Center
• 241 Pellham Street
• Portland, ME 04102
• Contact info: phone: 207-555-0148
• email: contact@brookmeadow.example
• www.vutel.example
• *The flyer must also include a picture of the speaker and our Vutel logo
Should not have
• Pictures of crosses or church buildings

```html
<!DOCTYPE html>
<html lang="en">
<head>
<meta charset="utf-8">
<title>Kestrel Summit 2019 – Flyer</title>
<link rel="stylesheet" href="https://fonts.googleapis.com/css2?family=Encode+Sans+Condensed:wght@400&family=Montserrat:wght@500;600&family=Open+Sans:wght@600&family=Oswald:wght@500&family=Source+Sans+3:wght@400;600&display=swap">
<style>
  :root {
    --backdrop: #d6d6d6;
    --navy: #0a0c40;
    --navy-soft: #172a55;
    --teal: #4bb8a0;
    --amber: #f7a80d;
    --pink: #f72d73;
    --crimson: #a5123f;
    --gold: #e8b42a;
    --date: #f5a81c;
    --white: #ffffff;
    --ink: #0d0d0d;
  }
  html, body { margin: 0; padding: 0; overflow: hidden; }
  body { background: var(--backdrop); }
  .canvas {
    position: relative;
    width: 943px;
    height: 1200px;
    background: var(--backdrop);
    overflow: hidden;
  }
  .shapes { position: absolute; inset: 0; width: 943px; height: 1200px; }
  .text { position: absolute; margin: 0; white-space: nowrap; line-height: 1; }

  .event-title {
    left: 381px; width: 411px; text-align: center;
    font-family: "Encode Sans Condensed", "Arial Narrow", sans-serif;
    font-size: 48px; font-weight: 400;
    background: linear-gradient(90deg, var(--navy) 0%, var(--crimson) 45%, var(--navy) 100%);
    -webkit-background-clip: text; background-clip: text; color: transparent;
  }
  .event-title.name { top: 80px; }
  .event-title.year { top: 133px; background: none; color: var(--crimson); }

  .topic {
    position: absolute; left: 418px; top: 213px; width: 359px; height: 26px;
    background: var(--ink); color: var(--white);
    font-family: "Oswald", "Arial Narrow", sans-serif; font-weight: 500;
    font-size: 18px; line-height: 26px; text-align: center; letter-spacing: -0.2px;
    margin: 0;
  }

  .session {
    left: 428px; color: var(--ink);
    font-family: "Oswald", "Arial Narrow", sans-serif; font-weight: 500;
    font-size: 20px; line-height: 30px; letter-spacing: -0.3px;
  }
  .session.one { top: 301px; }
  .session.two { top: 392px; }
  .session.three { top: 484px; }
  .session.four { top: 573px; }

  .brand {
    left: 135px; top: 276px; color: var(--navy);
    font-family: "Source Sans 3", sans-serif; font-weight: 600;
    font-size: 58px; letter-spacing: 2px;
  }

  .speaker-label, .speaker-title, .speaker-name {
    font-family: "Source Sans 3", sans-serif; font-weight: 400; color: var(--gold);
  }
  .speaker-label { left: 270px; top: 730px; font-size: 26px; }
  .speaker-title { left: 231px; top: 758px; font-size: 42px; }
  .speaker-name { left: 150px; top: 812px; font-size: 50px; }

  .schedule {
    right: 111px; text-align: right;
    font-family: "Montserrat", sans-serif; font-weight: 600; font-size: 30px;
  }
  .schedule.dates { top: 761px; color: var(--date); }
  .schedule.time { top: 803px; color: var(--white); }

  .venue {
    right: 112px; text-align: right; color: var(--white);
    font-family: "Montserrat", sans-serif; font-weight: 500; font-size: 26px;
  }
  .venue.hall { top: 896px; }
  .venue.street { top: 929px; }
  .venue.city { top: 962px; }

  .contact {
    top: 1092px; color: var(--white);
    font-family: "Open Sans", sans-serif; font-weight: 600; font-size: 17px;
  }
  .contact.phone { left: 143px; }
  .contact.email { left: 316px; }
  .contact.web { left: 618px; }
</style>
</head>
<body>
<div class="canvas">
  <svg class="shapes" viewBox="0 0 1708 2173" xmlns="http://www.w3.org/2000/svg">
    <defs>
      <clipPath id="flyer-clip"><rect x="168" y="115" width="1372" height="1943"/></clipPath>
      <linearGradient id="rule" x1="0" x2="1" y1="0" y2="0">
        <stop offset="0" stop-color="#0a0c40"/>
        <stop offset="0.5" stop-color="#f72d73"/>
        <stop offset="1" stop-color="#0a0c40"/>
      </linearGradient>
      <linearGradient id="portrait" x1="0" x2="0" y1="0" y2="1">
        <stop offset="0" stop-color="#e9e9ec"/>
        <stop offset="0.55" stop-color="#7a3a3e"/>
        <stop offset="1" stop-color="#3a3b42"/>
      </linearGradient>
    </defs>

    <rect class="flyer" x="168" y="115" width="1372" height="1943" fill="var(--navy)"/>

    <g clip-path="url(#flyer-clip)">
      <polygon class="accent-teal" points="190,165 285,70 378,165 285,260" fill="var(--teal)"/>
      <polygon class="accent-amber" points="455,168 530,95 602,168 530,242" fill="var(--amber)"/>
      <polygon class="accent-pink" points="168,215 248,290 168,362" fill="var(--pink)"/>

      <polygon class="logo-diamond" points="388,195 748,552 388,909 31,552" fill="var(--white)"/>

      <polygon class="portrait-frame" points="372,700 700,1028 372,1357 44,1028" fill="var(--teal)"/>
      <polygon class="portrait" points="372,748 660,1028 372,1310 84,1028" fill="url(#portrait)"
               role="img" aria-label="Portrait photo of the speaker, Prophet Marcus Toliver"/>

      <polygon class="star" points="497,1243 590,1395 790,1355 680,1520 765,1655 595,1615 462,1727 452,1570 296,1470 470,1395" fill="var(--navy-soft)"/>

      <polygon class="accent-amber" points="258,1285 348,1378 258,1470 168,1378" fill="var(--amber)"/>
      <polygon class="accent-pink" points="168,1455 360,1645 168,1838" fill="var(--pink)"/>

      <polygon class="banner-edge" points="650,115 1475,115 1475,1182 1062,1350 650,1182" fill="var(--pink)"/>
      <polygon class="banner" points="690,115 1435,115 1435,1140 1062,1290 690,1140" fill="var(--amber)"/>
    </g>

    <rect class="title-rule" x="745" y="329" width="665" height="6" fill="url(#rule)"/>
    <rect class="double-rule" x="897" y="485" width="352" height="5" fill="url(#rule)"/>
    <rect class="double-rule" x="897" y="499" width="352" height="5" fill="url(#rule)"/>
    <rect class="session-rule" x="917" y="680" width="288" height="13" rx="6.5" fill="url(#rule)"/>
    <rect class="session-rule" x="917" y="843" width="288" height="13" rx="6.5" fill="url(#rule)"/>
    <rect class="session-rule" x="917" y="986" width="288" height="13" rx="6.5" fill="url(#rule)"/>
    <rect class="session-rule" x="917" y="1144" width="288" height="13" rx="6.5" fill="url(#rule)"/>

    <g class="pin-icon" fill="none" stroke="var(--date)">
      <circle cx="928" cy="1740" r="47" stroke-width="6"/>
      <path d="M928 1775 L908 1738 A22 22 0 1 1 948 1738 Z" fill="var(--date)" stroke="none"/>
      <circle cx="928" cy="1728" r="8" fill="var(--navy)" stroke="none"/>
    </g>

    <rect class="footer-rule" x="212" y="1949" width="1240" height="5" fill="var(--white)"/>

    <g class="footer-icons" fill="none" stroke="var(--white)" stroke-width="4">
      <path d="M224 1988 q-6 8 4 22 q10 12 20 8 l3 -5 l-8 -7 l-5 4 q-8 -5 -11 -13 l4 -4 l-5 -9 z" fill="var(--white)" stroke="none"/>
      <path d="M236 1985 a14 14 0 0 1 12 12 M236 1978 a20 20 0 0 1 19 19" stroke-width="3"/>
      <rect x="525" y="1987" width="30" height="20"/>
      <path d="M525 1987 L540 1999 L555 1987 M525 2007 L536 1997 M555 2007 L544 1997" stroke-width="3"/>
      <circle cx="1088" cy="1995" r="15" stroke-width="3"/>
      <ellipse cx="1088" cy="1995" rx="6" ry="15" stroke-width="2.5"/>
      <path d="M1073 1995 H1103 M1076 1987 H1100 M1076 2003 H1100" stroke-width="2.5"/>
    </g>
  </svg>

  <h1 class="text event-title name">KESTREL SUMMIT</h1>
  <p class="text event-title year">2019</p>

  <h2 class="topic">THE ENEMIES OF THE END - TIMES CHURCH</h2>

  <p class="text session one">HOW THE ANTICHRIST RAISES AN ARMY BY<br>SOCIAL BEHAVIOR ENGINEERING</p>
  <p class="text session two">HOW THE ARCHITECTS OF MODERN SOCIAL<br>CONSTRUCTS ESCAPED THE CHURCH'S RADAR.</p>
  <p class="text session three">THE HOLY SPIRIT'S END - TIMES AGENDA</p>
  <p class="text session four">THE KNOCK - OUT PUNCH!</p>

  <p class="text brand">VUTEL</p>

  <p class="text speaker-label">Speaker</p>
  <p class="text speaker-title">PROPHET</p>
  <p class="text speaker-name">MARCUS TOLIVER</p>

  <p class="text schedule dates">December 27,28, &amp; 29th</p>
  <p class="text schedule time">@ 6:00 PM</p>

  <p class="text venue hall">Halvorn Community Center</p>
  <p class="text venue street">241 Pellham Street.</p>
  <p class="text venue city">Portland, ME 04102</p>

  <p class="text contact phone">207-555-0148</p>
  <p class="text contact email">contact@brookmeadow.example</p>
  <p class="text contact web">www.vutel.example</p>
</div>
</body>
</html>
```